Flyer for my live dj set from a recent party (party flyer included)

Need a recreation of a flyer for my live dj mix from the night of the party

(I added a pic of me and my logo if that looks good as well):

TEXT:

NO SITTING DOWN ON THE TILES HERE

MORVEL STUDIOS One Year Anniversary Party 2019

QUILLA (Closing Set)

Recorded Live at Brasswick Hollow Brewery

beatpage.net/quilla482

Target Market(s)

Electronic Music, Nightclub goers

Industry/Entity Type

Night Club

Font styles to use
Sans Serif

Colors

Designer to choose colors to be used in the design.

Requirements
Must have
• Elements of the original party flyer
Nice to have
• Some bright or neon, something that pops. Try to keep it similar to the flyer attached so it has the same theme and looks like a promo mix for that party

```html
<!DOCTYPE html>
<html lang="en">
<head>
<meta charset="utf-8">
<title>No Sitting Down On The Tiles Here – Morvel Studios Anniversary Mix</title>
<link href="https://fonts.googleapis.com/css2?family=Montserrat:wght@400;600;700;800&family=Open+Sans:wght@300;400;600&display=swap" rel="stylesheet">
<style>
  :root {
    --bg: #000000;
    --white: #ffffff;
    --blue: #1f4fd8;
    --blue-bright: #2a5cff;
    --warm-a: #5a2230;
    --warm-b: #2a1030;
    --brew-green: #3c5a32;
  }
  html, body {
    margin: 0;
    padding: 0;
    width: 848px;
    height: 1200px;
    overflow: hidden;
    background: var(--bg);
  }
  .flyer {
    position: relative;
    width: 848px;
    height: 1200px;
    background: var(--bg);
    overflow: hidden;
    font-family: "Montserrat", sans-serif;
    color: var(--white);
  }
  .stage-lights {
    position: absolute;
    left: 0; top: 0;
    width: 848px; height: 620px;
    background:
      radial-gradient(ellipse 220px 90px at 260px 380px, rgba(120,70,160,0.55), transparent 70%),
      radial-gradient(ellipse 160px 260px at 250px 120px, rgba(150,40,120,0.35), transparent 70%),
      radial-gradient(ellipse 120px 240px at 380px 140px, rgba(60,80,200,0.35), transparent 70%),
      linear-gradient(180deg, rgba(13,26,74,0.4), transparent 90%);
  }
  .dj-photo {
    position: absolute;
    left: 330px; top: 640px;
    width: 518px; height: 560px;
    background:
      radial-gradient(ellipse 200px 260px at 260px 260px, rgba(140,60,80,0.55), transparent 75%),
      linear-gradient(180deg, var(--warm-b) 0%, var(--warm-a) 55%, #140810 100%);
    -webkit-mask-image: radial-gradient(ellipse 300px 340px at 300px 320px, #000 55%, transparent 100%);
    mask-image: radial-gradient(ellipse 300px 340px at 300px 320px, #000 55%, transparent 100%);
  }

  .title { position: absolute; left: 54px; top: 84px; margin: 0; line-height: 1; }
  .title span { display: block; }
  .title-lead { font-weight: 800; font-size: 46px; letter-spacing: -0.5px; }
  .title-mid  { font-weight: 400; font-size: 40px; margin-top: 12px; }
  .title-end  { font-weight: 800; font-size: 52px; color: var(--blue); margin-top: 6px; letter-spacing: -0.5px; }

  .shades {
    position: absolute; left: 505px; top: 80px;
    width: 268px; height: 126px;
    border-radius: 40px;
    background: radial-gradient(ellipse at center, rgba(42,92,255,0.45), rgba(42,92,255,0.08) 70%);
  }

  .host { position: absolute; left: 54px; top: 252px; margin: 0; line-height: 1; }
  .host-name { font-weight: 800; font-size: 48px; color: var(--blue); }
  .host-sub  { font-weight: 400; font-size: 25px; }
  .host-line { display: block; font-weight: 400; font-size: 28px; margin-top: 6px; }
  .host-year { font-size: 36px; }

  .date-box {
    position: absolute; left: 52px; top: 386px;
    width: 238px; height: 106px;
    border: 2px solid var(--blue);
    box-sizing: border-box;
    color: var(--blue);
    font-weight: 800;
    padding: 12px 0 0 24px;
    line-height: 1;
  }
  .date-day  { font-size: 30px; display: block; }
  .date-time { font-size: 50px; display: block; margin-top: 2px; }

  .love-house { position: absolute; left: 410px; top: 398px; }

  .recorded { position: absolute; left: 54px; top: 516px; font-weight: 700; font-size: 20px; line-height: 1.05; }
  .headliner { position: absolute; left: 54px; top: 572px; color: var(--blue); line-height: 1; white-space: nowrap; }
  .headliner-name { font-weight: 800; font-size: 44px; letter-spacing: 1px; }
  .headliner-note { font-weight: 400; font-size: 38px; }
  .social { position: absolute; left: 56px; top: 622px; font-family: "Open Sans", sans-serif; font-size: 16px; }

  .lineup {
    position: absolute; left: 56px; top: 666px;
    margin: 0; padding: 0; list-style: none;
    font-family: "Open Sans", sans-serif; font-size: 17px; line-height: 30px;
  }

  .venue {
    position: absolute; left: 54px; top: 836px;
    font-family: "Open Sans", sans-serif; font-weight: 300;
    color: var(--blue-bright); font-size: 28px; line-height: 31px;
  }

  .brewery-mark {
    position: absolute; left: 54px; top: 1040px;
    display: flex; align-items: center; gap: 14px;
    font-family: "Montserrat", sans-serif; font-weight: 700; font-size: 15px;
    color: var(--white);
  }
  .brewery-dot { width: 60px; height: 60px; border-radius: 50%; background: var(--brew-green); }
</style>
</head>
<body>
<main class="flyer">
  <div class="stage-lights" role="img" aria-label="Dance floor with coloured stage spotlights and patterned light projections"></div>
  <div class="dj-photo" role="img" aria-label="Photo of the DJ performing at the decks under warm stage light"></div>

  <h1 class="title">
    <span class="title-lead">NO SITTING DOWN</span>
    <span class="title-mid">ON THE TILES</span>
    <span class="title-end">HERE</span>
  </h1>

  <div class="shades" role="img" aria-label="Neon blue shutter-shade party glasses illustration"></div>

  <p class="host">
    <span class="host-name">MORVEL</span> <span class="host-sub">STUDIOS</span>
    <span class="host-line">1 YEAR ANNIVERSARY</span>
    <span class="host-line">PARTY <span class="host-year">2019</span></span>
  </p>

  <div class="date-box">
    <span class="date-day">JAN. 19</span>
    <span class="date-time">5p-10p</span>
  </div>

  <svg class="love-house" width="390" height="80" viewBox="0 0 390 80" aria-label="I love house music">
    <text x="0" y="68" font-family="Georgia, serif" font-weight="700" font-size="74" fill="#ffffff">I</text>
    <path d="M114 72 L84 42 C72 30 80 12 96 12 C105 12 111 18 114 24 C117 18 123 12 132 12 C148 12 156 30 144 42 Z"
          fill="none" stroke="#1f4fd8" stroke-width="5" stroke-linejoin="round"/>
    <path d="M200 40 L237 8 L274 40" fill="none" stroke="#ffffff" stroke-width="9" stroke-linejoin="miter"/>
    <path d="M210 36 L210 72 L264 72 L264 36" fill="none" stroke="#ffffff" stroke-width="9"/>
    <rect x="228" y="50" width="18" height="22" fill="#ffffff"/>
    <path d="M334 16 L378 8 L378 58" fill="none" stroke="#ffffff" stroke-width="8"/>
    <path d="M334 12 L334 64" stroke="#ffffff" stroke-width="8"/>
    <ellipse cx="325" cy="66" rx="13" ry="10" fill="#ffffff"/>
    <ellipse cx="369" cy="60" rx="13" ry="10" fill="#ffffff"/>
    <path d="M334 12 L378 4 L378 18 L334 26 Z" fill="#ffffff"/>
  </svg>

  <div class="recorded">Recorded Live<br>@BrasswickHollowBrewery</div>
  <div class="headliner"><span class="headliner-name">QUILLA</span> <span class="headliner-note">(Closing Set)</span></div>
  <div class="social">beatpage.net/ quilla482</div>

  <ul class="lineup">
    <li>| QUILLA (Closing Set) |</li>
    <li>| VELLANO (TBR/Deeper Signal) |</li>
    <li>| TORVIA (LTS/Found In Motion) |</li>
    <li>| SOLAR DISPUTE (Morvel/Ground Drum) |</li>
  </ul>

  <div class="venue">
    21+w/ID<br>
    No Cover<br>
    2214 Larkmoor Blvd.<br>
    @BrasswickHollowBrewery
  </div>

  <div class="brewery-mark">
    <span class="brewery-dot"></span>
    <span>BRASSWICK HOLLOW BREWERY</span>
  </div>
</main>
</body>
</html>
```